Brightvantage.com tech company website

Current site is www.brightvantage.com. The site will tell you about our company.

Designs we like are:
http://megainfo.quellorix.com
www.trelvo.com
www.morvasket.com

Target Market(s)

B2B

Industry/Entity Type

It Company

Coding

Coded - Design and coding required

Number of Pages Required

5+ page

Requirements
Must have
• We want to entice without giving away too much info. We like graphics and colors. But website must look official and credible.

```html
<!DOCTYPE html>
<html lang="en">
<head>
<meta charset="utf-8">
<title>Brightvantage.com</title>
<link href="https://fonts.googleapis.com/css2?family=Raleway:wght@300;400;600;700&family=Open+Sans:wght@400;600;700&display=swap" rel="stylesheet">
<style>
:root{
  --navy:#1d4f7a;
  --nav-text:#4a4a4a;
  --blue:#1a9be0;
  --mustard:#d8a52e;
  --magenta:#c04fc4;
  --coral:#f15a3b;
  --black:#0c0c0c;
  --white:#ffffff;
  --soft-white:rgba(255,255,255,.88);
}
*{margin:0;padding:0;box-sizing:border-box}
html,body{width:1200px;height:2668px;overflow:hidden;background:var(--white)}
body{font-family:"Open Sans",Arial,sans-serif;color:var(--white)}
.page{width:1200px;height:2668px;position:relative}

/* header */
.site-header{height:68px;background:var(--white);display:flex;align-items:center;justify-content:space-between;padding:0 60px 0 22px}
.brand{display:flex;align-items:center;gap:10px;font-family:"Raleway",sans-serif;font-weight:700;font-size:24px;color:var(--navy);letter-spacing:.5px}
.brand-dot{width:14px;height:14px;border-radius:50%;background:var(--blue)}
.main-nav{display:flex;height:68px}
.main-nav a{display:flex;align-items:center;padding:0 18px;font-size:11px;font-weight:600;color:var(--nav-text);text-decoration:none;text-transform:uppercase;letter-spacing:.4px}
.main-nav a.active{background:var(--navy);color:var(--white);padding:0 26px}

/* hero */
.hero{position:relative;height:652px;background:linear-gradient(135deg,#c9d7e2 0%,#e9dccb 35%,#b7c7d3 60%,#8fa6b8 100%)}
.hero-photo{position:absolute;inset:0}
.hero-copy{position:absolute;left:560px;top:365px;width:600px;text-align:right}
.hero-copy h1{font-family:"Raleway",sans-serif;font-weight:400;font-size:40px;line-height:44px;text-transform:uppercase;letter-spacing:1px;text-shadow:0 1px 4px rgba(0,0,0,.35)}
.hero-copy p{margin-top:18px;font-size:12px;line-height:18px;color:var(--soft-white);text-align:left}
.hero-btn{position:absolute;right:50px;top:540px;background:var(--white);color:var(--coral);font-size:10px;font-weight:700;padding:9px 16px;text-transform:uppercase}
.hero-dots{position:absolute;right:50px;top:612px;display:flex;gap:10px}
.hero-dots span{width:10px;height:10px;border-radius:50%;border:1px solid var(--white)}
.hero-dots span.on{background:var(--white)}

/* shared */
.section-title{font-family:"Raleway",sans-serif;font-weight:400;font-size:36px;text-align:center}
.outline-btn{display:inline-block;border:1px solid var(--white);color:var(--white);font-size:10px;padding:9px 20px;text-transform:uppercase}
.body-copy{font-size:12px;line-height:20px;text-align:center;color:var(--soft-white)}

/* about */
.about{height:332px;background:var(--blue);padding:40px 80px 0;text-align:center}
.about .body-copy{margin:34px auto 0;width:1040px}
.about .outline-btn{margin-top:26px}

/* services */
.services{height:448px;background:var(--mustard);padding:40px 0 0}
.service-grid{display:flex;justify-content:center;gap:60px;margin-top:38px}
.service{width:320px;text-align:center}
.service-thumb{width:104px;height:104px;border-radius:50%;margin:0 auto;border:3px solid var(--white)}
.thumb-marketing{background:linear-gradient(160deg,#2a5c8a,#dde6ee)}
.thumb-leads{background:linear-gradient(160deg,#f4f4f4,#c8b89a)}
.thumb-data{background:linear-gradient(160deg,#3a3a3a,#7a6a5a)}
.service h3{margin-top:16px;font-size:12px;font-weight:700;text-transform:uppercase}
.service p{margin-top:10px;font-size:11px;line-height:17px;color:var(--soft-white)}
.service .outline-btn{margin-top:26px}

/* advisors */
.advisors{height:520px;background:var(--magenta);padding:40px 0 0}
.advisors .body-copy{width:1000px;margin:22px auto 0}
.advisors h4{margin-top:34px;text-align:center;font-size:18px;font-weight:700}
.capability-lists{display:flex;justify-content:center;gap:60px;margin-top:24px}
.capability-lists ul{list-style:none;width:420px}
.capability-lists li{position:relative;padding-left:20px;font-size:11px;line-height:16px;margin-bottom:14px;color:var(--soft-white)}
.capability-lists li::before{content:"";position:absolute;left:0;top:5px;width:6px;height:6px;border-radius:50%;background:var(--white)}

/* lower split */
.split{display:flex;height:420px}
.team-visual{width:600px;background:linear-gradient(180deg,#3a7fc4 0%,#8cc3ea 55%,#dbeefa 100%)}
.case-studies{width:600px;background:var(--coral);padding:44px 50px 0}
.case-studies h2{font-family:"Raleway",sans-serif;font-weight:400;font-size:34px;text-align:center}
.case-list{list-style:none;margin-top:34px}
.case-list li{display:flex;align-items:flex-start;gap:10px;font-size:12px;line-height:16px;margin-bottom:12px}
.case-list svg{flex:none;margin-top:2px}

/* footer */
.site-footer{height:228px;background:var(--black);text-align:center;padding-top:26px}
.site-footer h2{font-family:"Raleway",sans-serif;font-weight:400;font-size:30px}
.contact-line{margin-top:18px;font-size:11px;line-height:18px}
.footer-nav{margin-top:20px;display:flex;justify-content:center;gap:8px;font-size:11px;font-weight:600}
.footer-nav a{color:var(--white);text-decoration:none}
.copyright{margin-top:26px;font-size:10px;color:#aaaaaa}
</style>
</head>
<body>
<div class="page">

  <header class="site-header">
    <div class="brand"><span class="brand-dot"></span>Brightvantage</div>
    <nav class="main-nav">
      <a href="#" class="active">Home</a>
      <a href="#">About Us</a>
      <a href="#">Big Data and Analytics</a>
      <a href="#">Perception and Influence</a>
      <a href="#">Case Studies</a>
      <a href="#">Contact Us</a>
    </nav>
  </header>

  <section class="hero">
    <div class="hero-photo" role="img" aria-label="Photo of a smiling team of young professionals working together at a laptop in a bright office"></div>
    <div class="hero-copy">
      <h1>Consectetur adipiscing<br>lorem ipsum dolor</h1>
      <p>Lorem ipsum dolor sit amet, consectetur adipiscing elit, sed do eiusmod tempor incididunt ut labore et dolore magna aliqua. Ut enim ad minim veniam, quis nostrud exercitation ullamco laboris nisi aliquip.</p>
    </div>
    <span class="hero-btn">Read more</span>
    <div class="hero-dots"><span></span><span></span><span></span><span class="on"></span><span></span></div>
  </section>

  <section class="about">
    <h2 class="section-title">About us</h2>
    <p class="body-copy">Lorem ipsum dolor sit amet, consectetur adipiscing elit, sed do eiusmod tempor incididunt ut labore et dolore magna aliqua. Ut enim ad minim veniam, quis nostrud exercitation ullamco laboris nisi ut aliquip ex ea commodo consequat. Duis aute irure dolor in reprehenderit in voluptate velit esse cillum dolore eu fugiat nulla pariatur. Excepteur sint occaecat cupidatat non proident, sunt in culpa qui officia deserunt mollit anim id est laborum. Sed ut perspiciatis unde omnis iste natus error sit voluptatem accusantium doloremque laudantium, totam rem aperiam, eaque ipsa quae ab illo inventore veritatis et quasi architecto beatae vitae dicta sunt explicabo. Nemo enim ipsam voluptatem quia voluptas sit aspernatur aut odit aut fugit, sed quia consequuntur magni dolores eos qui ratione.</p>
    <span class="outline-btn">Read more</span>
  </section>

  <section class="services">
    <h2 class="section-title">Our Service</h2>
    <div class="service-grid">
      <div class="service">
        <div class="service-thumb thumb-marketing" role="img" aria-label="Portrait photo of a businesswoman"></div>
        <h3>Precision Reach Marketing</h3>
        <p>Lorem ipsum dolor sit amet, consectetur adipiscing elit, sed do eiusmod tempor incididunt ut labore et dolore magna aliqua enim minim veniam.</p>
        <span class="outline-btn">Read more</span>
      </div>
      <div class="service">
        <div class="service-thumb thumb-leads" role="img" aria-label="Photo of a gauge reading lead generation"></div>
        <h3>Lead Generation</h3>
        <p>Quis nostrud exercitation ullamco laboris nisi ut aliquip ex ea commodo consequat duis aute irure dolor in reprehenderit voluptate.</p>
        <span class="outline-btn">Read more</span>
      </div>
      <div class="service">
        <div class="service-thumb thumb-data" role="img" aria-label="Photo of a hand writing data notes"></div>
        <h3>Data Enhancement</h3>
        <p>Excepteur sint occaecat cupidatat non proident, sunt in culpa qui officia deserunt mollit anim id est laborum sed perspiciatis unde.</p>
        <span class="outline-btn">Read more</span>
      </div>
    </div>
  </section>

  <section class="advisors">
    <h2 class="section-title">Board of Advisors</h2>
    <p class="body-copy">Nemo enim ipsam voluptatem quia voluptas sit aspernatur aut odit aut fugit, sed quia consequuntur magni dolores eos qui ratione voluptatem sequi nesciunt. Neque porro quisquam est, qui dolorem ipsum quia dolor sit amet, consectetur, adipisci velit, sed quia non numquam eius modi tempora.</p>
    <h4>What can we do? Here's a partial list:</h4>
    <div class="capability-lists">
      <ul>
        <li>Make people feel positively about you and your company</li>
        <li>Change the conversation away from issues you want minimized</li>
        <li>Create buzz, launch, and demand for products and services</li>
        <li>Move business rivals to unfavorable positions in the eyes of public opinion</li>
      </ul>
      <ul>
        <li>Repair tarnished reputations</li>
        <li>Move retail prices</li>
        <li>Generate traffic to a website or physical location</li>
        <li>Beat rivals</li>
      </ul>
    </div>
  </section>

  <section class="split">
    <div class="team-visual" role="img" aria-label="Illustration of business people silhouettes standing before a world map"></div>
    <div class="case-studies">
      <h2>Case Studies</h2>
      <ul class="case-list">
        <li><svg width="12" height="12" viewBox="0 0 12 12"><path d="M1 6l3.5 3.5L11 2" fill="none" stroke="#fff" stroke-width="2"/></svg>Maintained share value for Fortune 500 Company under regulatory duress</li>
        <li><svg width="12" height="12" viewBox="0 0 12 12"><path d="M1 6l3.5 3.5L11 2" fill="none" stroke="#fff" stroke-width="2"/></svg>Initial Public Offering Management for Financial Services Co.</li>
        <li><svg width="12" height="12" viewBox="0 0 12 12"><path d="M1 6l3.5 3.5L11 2" fill="none" stroke="#fff" stroke-width="2"/></svg>Increased sales with our Precision Reach Marketing program</li>
        <li><svg width="12" height="12" viewBox="0 0 12 12"><path d="M1 6l3.5 3.5L11 2" fill="none" stroke="#fff" stroke-width="2"/></svg>Customized solution for increased leads and revenue for startup</li>
        <li><svg width="12" height="12" viewBox="0 0 12 12"><path d="M1 6l3.5 3.5L11 2" fill="none" stroke="#fff" stroke-width="2"/></svg>Risk Characterization for Supply Chain</li>
        <li><svg width="12" height="12" viewBox="0 0 12 12"><path d="M1 6l3.5 3.5L11 2" fill="none" stroke="#fff" stroke-width="2"/></svg>Minimized reputational risk and enhanced sentiment for high profile family</li>
      </ul>
    </div>
  </section>

  <footer class="site-footer">
    <h2>Contact</h2>
    <p class="contact-line">To find out how we can maximize your outcomes call 555.014.2290<br>Or email info@brightvantage.com</p>
    <nav class="footer-nav">
      <a href="#">Home</a><span>|</span><a href="#">About Us</a><span>|</span><a href="#">Big Data and Analytics</a><span>|</span><a href="#">Perception and Influence</a><span>|</span><a href="#">Case Studies</a><span>|</span><a href="#">Contact Us</a>
    </nav>
    <p class="copyright">All Rights Reserved. Copyright ©2015 Company Name</p>
  </footer>

</div>
</body>
</html>
```